New Business Card Design Project

I would like my card design to look exactly like the logo, design, layout, and print of the current attached file. The only change I would like made would be for the print to say THE KMW GROUP instead of THE HALLORAN GROUP. Basically, just replace his group name with my group name. I would also like the backgroud to be the same texture and color as the attached file. I love the dark blue lettering and house logo on the card.

I am completely open to the rest of the card design. I just want something clean and simple. Only basic contact info required on the card. Maybe just name: Kyle M Warrick and cell # 555.914.2087 and email kyle@orchidhomesagent.com

```html
<!DOCTYPE html>
<html lang="en">
<head>
<meta charset="utf-8">
<title>The KMW Group – Business Card</title>
<link rel="stylesheet" href="https://fonts.googleapis.com/css2?family=Open+Sans:wght@300;400&display=swap">
<style>
  :root {
    --backdrop: #b8afa8;
    --card: #e8e7e4;
    --card-edge: #d6d4d0;
    --ink: #1a1c33;
  }
  * { margin: 0; padding: 0; box-sizing: border-box; }
  html, body { width: 1200px; height: 900px; overflow: hidden; }
  body {
    position: relative;
    background: var(--backdrop);
    font-family: "Open Sans", Arial, sans-serif;
    color: var(--ink);
  }
  .card {
    position: absolute;
    width: 500px;
    height: 286px;
    background: var(--card);
    border: 1px solid var(--card-edge);
    box-shadow: 0 3px 0 var(--card-edge), 0 6px 0 #cfccc8;
  }
  .card--front { left: 90px; top: 440px; }
  .card--back { left: 610px; top: 170px; }

  /* Front: group name */
  .brand {
    position: absolute;
    left: 118px;
    top: 92px;
    display: flex;
    align-items: center;
    gap: 26px;
  }
  .brand__square {
    width: 72px;
    height: 72px;
    background: var(--ink);
  }
  .brand__name {
    font-weight: 300;
    font-size: 22px;
    line-height: 28px;
    letter-spacing: 6px;
    text-transform: uppercase;
  }

  /* Back: name and contacts */
  .rule {
    position: absolute;
    left: 0;
    top: 58px;
    width: 330px;
    height: 1.5px;
    background: var(--ink);
  }
  .person {
    position: absolute;
    right: 30px;
    top: 70px;
    font-weight: 400;
    font-size: 24px;
    letter-spacing: 7px;
    text-transform: uppercase;
    white-space: nowrap;
  }
  .contacts {
    position: absolute;
    left: 250px;
    top: 206px;
    list-style: none;
    font-size: 13px;
    line-height: 24px;
  }
  .contacts li { display: flex; align-items: center; gap: 9px; }
  .contacts svg { width: 14px; height: 14px; flex: none; }
</style>
</head>
<body>
  <section class="card card--front" aria-label="Card front">
    <div class="brand">
      <span class="brand__square" aria-hidden="true"></span>
      <p class="brand__name">The<br>KMW<br>Group</p>
    </div>
  </section>

  <section class="card card--back" aria-label="Card back">
    <span class="rule" aria-hidden="true"></span>
    <h1 class="person">Kyle M Warrick</h1>
    <ul class="contacts">
      <li>
        <svg viewBox="0 0 14 14" aria-hidden="true"><rect x="3.5" y="0.8" width="7" height="12.4" rx="1.2" fill="none" stroke="#1a1c33" stroke-width="1"/><line x1="6" y1="11" x2="8" y2="11" stroke="#1a1c33" stroke-width="1"/></svg>
        <span>555.914.2087</span>
      </li>
      <li>
        <svg viewBox="0 0 14 14" aria-hidden="true"><rect x="0.8" y="2.8" width="12.4" height="8.4" fill="none" stroke="#1a1c33" stroke-width="1"/><polyline points="0.8,2.8 7,7.6 13.2,2.8" fill="none" stroke="#1a1c33" stroke-width="1"/></svg>
        <span>kyle@orchidhomesagent.com</span>
      </li>
    </ul>
  </section>
</body>
</html>
```